Sales Website Design

Create a sales-oriented website to advertise turn-key solutions for providing infection control to senior housing operators. There are several items uploaded. The pdf should serve as your guide. The powerpoint presentation has additional information.

The idea is this is senior housing reimagined for infection control. The design should be sleek, clean, vibrant and energetic.

Our goal is to sell a turnkey solution for making buildings safer for residents, staff, and families.

Target Market(s)

People who own and operate senior housing communities

```html
<!DOCTYPE html>
<html lang="en">
<head>
<meta charset="utf-8">
<title>Sagecare – Senior Housing Reimagined for Infection Control</title>
<link rel="stylesheet" href="https://fonts.googleapis.com/css2?family=Barlow+Semi+Condensed:wght@500;600;700&family=Heebo:wght@400;500;700&display=swap">
<style>
:root{
  --navy:#15196b;
  --navy-deep:#12165e;
  --teal:#1a9e9b;
  --teal-light:#5cc3bf;
  --ink:#222;
  --muted:#555;
  --card:#ffffff;
  --soft:#eeeeee;
  --line:#e3e3e3;
}
*{box-sizing:border-box;margin:0;padding:0}
html,body{width:1200px;height:3997px;overflow:hidden}
body{position:relative;background:#fff;font-family:"Heebo",Arial,sans-serif;color:var(--ink)}
.abs{position:absolute}
.display{font-family:"Barlow Semi Condensed","Arial Narrow",sans-serif;font-weight:700}
.accent{color:var(--teal)}
.section-title{position:absolute;left:0;width:1200px;text-align:center;font-family:"Barlow Semi Condensed","Arial Narrow",sans-serif;font-weight:700;font-size:38px;color:var(--navy);letter-spacing:.5px}

/* header */
.topline{left:0;top:0;width:1200px;height:5px;background:var(--teal)}
.site-header{left:0;top:5px;width:1200px;height:90px;background:#fff}
.brand{left:111px;top:32px;font-family:"Barlow Semi Condensed",sans-serif;font-weight:700;font-size:22px;color:var(--navy);letter-spacing:.5px}
.main-nav{left:312px;top:37px;display:flex;gap:18px;font-size:14px;font-weight:500;color:#111}
.main-nav .active{color:var(--teal);border-bottom:2px solid var(--teal);padding-bottom:5px}
.phone-pill{left:928px;top:30px;width:161px;height:40px;border-radius:20px;background:var(--teal);color:#fff;font-size:14px;font-weight:500;display:flex;align-items:center;padding-left:6px;gap:10px}
.phone-pill .dot{width:30px;height:30px;border-radius:50%;background:var(--navy);display:flex;align-items:center;justify-content:center}

/* hero */
.hero{left:0;top:95px;width:1200px;height:586px;background:linear-gradient(180deg,#5a86b8 0%,#9fb9d6 28%,#7f8d8c 45%,#5f6f5e 62%,#4b6d2f 78%,#5d8a33 100%)}
.hero-panel{left:352px;top:277px;width:506px;height:222px;background:rgba(28,28,140,.72);text-align:center;color:#fff}
.hero-panel h1{font-family:"Barlow Semi Condensed",sans-serif;font-weight:700;font-size:42px;margin-top:20px;letter-spacing:.5px}
.hero-panel p{font-size:15px;font-weight:500;line-height:24px;margin:6px auto 0;width:440px}
.btn-start{left:507px;top:425px;width:186px;height:45px;border-radius:23px;background:var(--teal);color:#fff;font-size:15px;font-weight:700;display:flex;align-items:center;justify-content:center;gap:8px}
.slide-arrow{top:368px;width:42px;height:42px;border-radius:50%;border:2px solid #fff;display:flex;align-items:center;justify-content:center}

/* technology */
.tech-card{position:absolute;width:312px;height:188px;background:var(--card);box-shadow:0 2px 10px rgba(0,0,0,.12);display:flex;flex-direction:column;align-items:center;justify-content:center;text-align:center}
.tech-card h3{font-family:"Barlow Semi Condensed",sans-serif;font-weight:700;font-size:17px;color:#111;letter-spacing:.3px;line-height:21px;margin-top:12px}
.tech-card.featured{background:var(--teal);color:#fff;padding:0 30px}
.tech-card.featured h3{color:#fff;margin:0 0 12px}
.tech-card.featured p{font-size:12.5px;line-height:21px}
.icon-ph{border-radius:8px;background:linear-gradient(135deg,#d6e6f0,#b9cde0)}

/* products */
.product{position:absolute;top:1432px;width:236px;height:376px;background:var(--soft);text-align:center}
.product .photo{margin:11px auto 0;width:215px;height:158px}
.product h3{font-size:15px;font-weight:500;color:#111;margin-top:26px}
.product p{font-size:12.5px;line-height:22px;color:var(--muted);margin:8px 12px 0;height:66px;overflow:hidden}
.btn-outline{display:inline-flex;align-items:center;gap:6px;margin-top:26px;height:42px;width:152px;justify-content:center;border:2px solid var(--teal);border-radius:21px;color:var(--teal);font-size:13px;font-weight:700;background:#fff}

/* benefits */
.benefits{left:0;top:1988px;width:1200px;height:344px;display:flex}
.benefit{width:300px;height:344px;color:#fff;text-align:center;padding:50px 20px 0}
.benefit.navy{background:var(--navy)}
.benefit.teal{background:var(--teal)}
.benefit h3{font-size:17px;font-weight:700;margin-top:14px}
.benefit p{font-size:13px;line-height:19px;margin-top:8px}
.benefit p+p{margin-top:3px}
.benefit .more{display:inline-flex;align-items:center;gap:6px;font-size:14px;font-weight:700;margin-top:18px}

/* process */
.step{position:absolute;width:270px;font-size:12.5px;line-height:21px;color:var(--muted)}
.step h4{font-size:15.5px;font-weight:500;color:#111;margin-bottom:6px;letter-spacing:.2px}
.step.left{text-align:right}
.step-icon{position:absolute;width:60px;height:60px;border-radius:50%;background:var(--navy);border:3px solid #fff;box-shadow:0 0 0 2px #dfe3f2;display:flex;align-items:center;justify-content:center}

/* case study */
.case{position:absolute;top:3148px;width:310px;height:368px;background:#fff;box-shadow:0 2px 10px rgba(0,0,0,.12)}
.case .photo{width:310px;height:190px}
.case .date{position:absolute;left:15px;top:175px;background:var(--teal);color:#fff;font-size:11.5px;padding:0 17px;height:32px;line-height:32px}
.case h3{font-size:17px;font-weight:400;color:#111;margin:28px 16px 0;font-family:Arial,sans-serif}
.case p{font-size:14px;line-height:23px;color:#777;margin:12px 16px 0;font-family:Arial,sans-serif}
.case .link{display:inline-flex;gap:6px;align-items:center;margin:14px 16px 0;font-size:15px;font-weight:700;color:var(--teal);font-family:Arial,sans-serif}

/* footer */
.site-footer{left:0;top:3625px;width:1200px;height:372px;background:var(--navy);color:#fff}
.site-footer h4{font-size:17px;font-weight:500}
.foot-brand{left:111px;top:88px;font-family:"Barlow Semi Condensed",sans-serif;font-weight:700;font-size:26px;letter-spacing:.5px}
.foot-about{left:111px;top:140px;width:200px;font-size:12.5px;line-height:19px}
.social{left:111px;top:240px;display:flex;gap:16px}
.contact-item{display:flex;gap:12px;font-size:12px;line-height:17px;margin-bottom:18px}
.contact-item b{font-weight:700;font-size:11.5px}
.foot-links{font-size:12.5px;line-height:26px;margin-top:20px}
.btn-touch{width:199px;height:40px;border-radius:20px;background:var(--teal);display:flex;align-items:center;justify-content:center;font-size:15px;font-weight:500;margin-top:30px}
.go-up{left:1007px;top:275px;width:80px;height:20px;border-radius:10px;background:#fff;color:var(--navy);font-size:11px;font-weight:700;display:flex;align-items:center;justify-content:center;gap:4px}
.legal{left:111px;top:344px;width:976px;display:flex;justify-content:space-between;font-size:13px}
</style>
</head>
<body>

<div class="abs topline"></div>
<header class="abs site-header">
  <div class="abs brand">SAGECARE</div>
  <nav class="abs main-nav">
    <span class="active">Home</span><span>Products</span><span>Technology</span><span>Benefits</span><span>Marketing</span><span>Process</span><span>Case study</span><span>Contact</span>
  </nav>
  <div class="abs phone-pill">
    <span class="dot"><svg width="14" height="14" viewBox="0 0 24 24"><path fill="#fff" d="M6.6 10.8a15 15 0 006.6 6.6l2.2-2.2c.3-.3.7-.4 1-.2 1.1.4 2.3.6 3.6.6.6 0 1 .4 1 1V20c0 .6-.4 1-1 1A17 17 0 013 4c0-.6.4-1 1-1h3.5c.6 0 1 .4 1 1 0 1.3.2 2.5.6 3.6.1.3 0 .7-.2 1z"/></svg></span>
    8888 888 8888
  </div>
</header>

<section class="abs hero" role="img" aria-label="Photo of a grey two-storey suburban home with a blue front door, green lawn and trees under a blue sky"></section>
<div class="abs hero-panel">
  <h1>SAGECARE</h1>
  <p>We are selling turnkey solutions to make senior housing facilities safer for staff, residents and family.</p>
</div>
<div class="abs btn-start">GET STARTED
  <svg width="16" height="16" viewBox="0 0 16 16"><circle cx="8" cy="8" r="8" fill="#fff"/><path d="M6 4.5L9.5 8 6 11.5" stroke="#1a9e9b" stroke-width="2" fill="none"/></svg>
</div>
<div class="abs slide-arrow" style="left:31px"><svg width="12" height="16"><path d="M9 2L3 8l6 6" stroke="#fff" stroke-width="2" fill="none"/></svg></div>
<div class="abs slide-arrow" style="left:1127px"><svg width="12" height="16"><path d="M3 2l6 6-6 6" stroke="#fff" stroke-width="2" fill="none"/></svg></div>

<!-- technology -->
<h2 class="section-title" style="top:772px">SAGECARE <span class="accent">TECHNOLOGY</span></h2>

<div class="tech-card" style="left:110px;top:853px">
  <div class="icon-ph" style="width:96px;height:54px" role="img" aria-label="Line icon of a temperature scanner pointed at a person"></div>
  <h3>TOUCHLESS TEMPERATURE<br>SCANS</h3>
</div>
<div class="tech-card featured" style="left:443px;top:853px">
  <h3>WIRELESS DIAGNOSTIC<br>EQUIPMENT</h3>
  <p>Lorem ipsum dolor sit amet, consectetur adipiscing elit, sed do eiusmod tempor incididunt ut labore et aliqua.</p>
</div>
<div class="tech-card" style="left:775px;top:853px">
  <svg width="70" height="62" viewBox="0 0 70 62"><rect x="3" y="3" width="64" height="42" rx="3" fill="none" stroke="#15196b" stroke-width="3"/><path d="M10 26h14l4-8 6 16 5-12 3 4h18" fill="none" stroke="#1a9e9b" stroke-width="3"/><path d="M28 45v8h14v-8M20 58h30" stroke="#15196b" stroke-width="3" fill="none"/></svg>
  <h3>WEARABLE MONITORING</h3>
</div>
<div class="tech-card" style="left:277px;top:1068px">
  <svg width="56" height="62" viewBox="0 0 56 62"><rect x="8" y="24" width="26" height="34" rx="4" fill="none" stroke="#15196b" stroke-width="3"/><path d="M14 24v-8h14v8M14 16l-2-8h20l6 4" fill="none" stroke="#15196b" stroke-width="3"/><path d="M21 34v14M14 41h14" stroke="#1a9e9b" stroke-width="3"/><circle cx="46" cy="8" r="3" fill="#1a9e9b"/><circle cx="50" cy="18" r="2.5" fill="#1a9e9b"/><circle cx="44" cy="22" r="2" fill="#1a9e9b"/></svg>
  <h3>DISINFECTANT EQUIPMENT</h3>
</div>
<div class="tech-card" style="left:612px;top:1068px">
  <svg width="56" height="64" viewBox="0 0 56 64"><rect x="23" y="4" width="10" height="48" rx="3" fill="none" stroke="#15196b" stroke-width="3"/><path d="M18 60h20" stroke="#15196b" stroke-width="3"/><path d="M6 18l10 4M4 30h11M6 42l10-4M50 18l-10 4M52 30H41M50 42l-10-4" stroke="#1a9e9b" stroke-width="3"/></svg>
  <h3>UV SANITATION DEVICES</h3>
</div>

<!-- products -->
<h2 class="section-title" style="top:1358px">OUR <span class="accent">PRODUCTS</span></h2>

<article class="product" style="left:111px">
  <div class="photo" role="img" aria-label="Photo of a pump bottle of hand sanitizer and a face mask" style="background:linear-gradient(160deg,#e9f3fa,#8fc1e3 60%,#2f73b0)"></div>
  <h3>Branded Signage</h3>
  <p>Custom branded signage installed throughout the building will help encourage staff, residents</p>
  <span class="btn-outline">READ MORE <svg width="12" height="12"><circle cx="6" cy="6" r="5" fill="none" stroke="#1a9e9b" stroke-width="1.5"/><path d="M5 3.5L7.5 6 5 8.5" stroke="#1a9e9b" stroke-width="1.5" fill="none"/></svg></span>
</article>
<article class="product" style="left:358px">
  <div class="photo" role="img" aria-label="Photo of an elevator entrance beside a small gold air purifier" style="background:linear-gradient(90deg,#1c1c1c,#3c3c3c 45%,#6a5a48 70%,#2a2a2a)"></div>
  <h3>Touchless Options</h3>
  <p>The fewer surfaces touched, the less opportunity to spread germs. Touchless technology is not</p>
  <span class="btn-outline">READ MORE <svg width="12" height="12"><circle cx="6" cy="6" r="5" fill="none" stroke="#1a9e9b" stroke-width="1.5"/><path d="M5 3.5L7.5 6 5 8.5" stroke="#1a9e9b" stroke-width="1.5" fill="none"/></svg></span>
</article>
<article class="product" style="left:605px">
  <div class="photo" role="img" aria-label="Photo of a wall-mounted air sanitation unit" style="background:radial-gradient(circle at 50% 50%,#d9c8c6 0%,#c0aeac 30%,#fafafa 60%)"></div>
  <h3>Air Sanitation</h3>
  <p>Eliminate airborne threats by installing air sanitation solutions that incorporates both</p>
  <span class="btn-outline">READ MORE <svg width="12" height="12"><circle cx="6" cy="6" r="5" fill="none" stroke="#1a9e9b" stroke-width="1.5"/><path d="M5 3.5L7.5 6 5 8.5" stroke="#1a9e9b" stroke-width="1.5" fill="none"/></svg></span>
</article>
<article class="product" style="left:852px">
  <div class="photo" role="img" aria-label="Photo of an office with clear protective dividers between desks" style="background:linear-gradient(180deg,#2a2a2a,#9a9a9a 40%,#d6d6d6 70%,#7b7b7b)"></div>
  <h3>Custom Dividers</h3>
  <p>Social distancing is effective, but not always possible. Dividers are a functional, cost-effective,</p>
  <span class="btn-outline">READ MORE <svg width="12" height="12"><circle cx="6" cy="6" r="5" fill="none" stroke="#1a9e9b" stroke-width="1.5"/><path d="M5 3.5L7.5 6 5 8.5" stroke="#1a9e9b" stroke-width="1.5" fill="none"/></svg></span>
</article>

<!-- benefits -->
<h2 class="section-title" style="top:1903px">SAGECARE <span class="accent">BENEFITS</span></h2>

<section class="abs benefits">
  <div class="benefit navy">
    <svg width="58" height="58" viewBox="0 0 58 58"><path d="M5 26L29 6l24 20" fill="none" stroke="#fff" stroke-width="3"/><rect x="10" y="24" width="38" height="30" fill="none" stroke="#fff" stroke-width="3"/><rect x="24" y="36" width="10" height="18" fill="none" stroke="#fff" stroke-width="2.5"/><rect x="14" y="30" width="7" height="7" fill="none" stroke="#fff" stroke-width="2"/><rect x="37" y="30" width="7" height="7" fill="none" stroke="#fff" stroke-width="2"/></svg>
    <h3>Residents</h3>
    <p>Positive impact on social determinants of health</p>
    <p>Increased ability to engage in social activities</p>
    <p>Greater sense of safety and dignity</p>
    <span class="more">LEARN MORE <svg width="13" height="13"><circle cx="6.5" cy="6.5" r="6.5" fill="#fff"/><path d="M5 3.5L8 6.5 5 9.5" stroke="#15196b" stroke-width="1.8" fill="none"/></svg></span>
  </div>
  <div class="benefit teal">
    <div role="img" aria-label="Line icon of a family group" style="width:70px;height:58px;margin:0 auto;border:3px solid #fff;border-radius:30px 30px 6px 6px;opacity:.9"></div>
    <h3>Family &amp; Friends</h3>
    <p>Reduce feelings of guilt when a loved one chooses a senior living setting</p>
    <p>Convenience ( virtual “shopping” platform ) Promote safe &amp; healthy visits</p>
    <p>Peace of mind</p>
    <span class="more">LEARN MORE <svg width="13" height="13"><circle cx="6.5" cy="6.5" r="6.5" fill="#fff"/><path d="M5 3.5L8 6.5 5 9.5" stroke="#1a9e9b" stroke-width="1.8" fill="none"/></svg></span>
  </div>
  <div class="benefit navy">
    <div role="img" aria-label="Line icon of a staff member" style="width:48px;height:58px;margin:0 auto;border:3px solid #fff;border-radius:24px 24px 6px 6px;opacity:.9"></div>
    <h3>Staff</h3>
    <p>Positive impact on social determinants of health</p>
    <p>Increased ability to engage in social activities</p>
    <p>Greater sense of safety and dignity</p>
    <span class="more">LEARN MORE <svg width="13" height="13"><circle cx="6.5" cy="6.5" r="6.5" fill="#fff"/><path d="M5 3.5L8 6.5 5 9.5" stroke="#15196b" stroke-width="1.8" fill="none"/></svg></span>
  </div>
  <div class="benefit teal">
    <div role="img" aria-label="Line icon of a corporate team" style="width:64px;height:58px;margin:0 auto;border:3px solid #fff;border-radius:30px 30px 6px 6px;opacity:.9"></div>
    <h3>Owners / Corporate</h3>
    <p>Positive impact on social determinants of health</p>
    <p>Increased ability to engage in social activities</p>
    <p>Greater sense of safety and dignity</p>
    <span class="more">LEARN MORE <svg width="13" height="13"><circle cx="6.5" cy="6.5" r="6.5" fill="#fff"/><path d="M5 3.5L8 6.5 5 9.5" stroke="#1a9e9b" stroke-width="1.8" fill="none"/></svg></span>
  </div>
</section>

<!-- process -->
<h2 class="section-title" style="top:2431px">SAGECARE <span class="accent">PROCESS</span></h2>

<svg class="abs" style="left:400px;top:2484px" width="400" height="400" viewBox="0 0 400 400">
  <circle cx="200" cy="200" r="176" fill="none" stroke="#9fd6d4" stroke-width="1.5" stroke-dasharray="3 4"/>
  <circle cx="200" cy="200" r="152" fill="#e3f4f3"/>
  <circle cx="200" cy="200" r="143" fill="#a9dcd9"/>
  <circle cx="200" cy="200" r="133" fill="#fff"/>
  <circle cx="200" cy="200" r="127" fill="#5cc3bf"/>
  <circle cx="200" cy="200" r="115" fill="#1a9e9b"/>
  <text x="200" y="212" text-anchor="middle" font-family="Barlow Semi Condensed, sans-serif" font-weight="700" font-size="32" fill="#fff" letter-spacing=".5">SAGECARE</text>
</svg>

<div class="step-icon" style="left:412px;top:2556px"><svg width="28" height="28"><rect x="5" y="3" width="18" height="22" rx="2" fill="none" stroke="#fff" stroke-width="2"/><path d="M9 10h10M9 15h10M9 20h6" stroke="#fff" stroke-width="2"/></svg></div>
<div class="step-icon" style="left:725px;top:2556px"><svg width="28" height="28"><rect x="3" y="5" width="22" height="15" rx="2" fill="none" stroke="#fff" stroke-width="2"/><path d="M8 24h12M7 14l4-4 3 3 5-5" stroke="#fff" stroke-width="2" fill="none"/></svg></div>
<div class="step-icon" style="left:412px;top:2740px"><svg width="28" height="28"><rect x="3" y="4" width="22" height="20" rx="2" fill="none" stroke="#fff" stroke-width="2"/><path d="M7 10h14M7 15h8M7 20h11" stroke="#fff" stroke-width="2"/></svg></div>
<div class="step-icon" style="left:725px;top:2740px"><svg width="28" height="28"><circle cx="14" cy="12" r="8" fill="none" stroke="#fff" stroke-width="2"/><circle cx="14" cy="12" r="3" fill="#fff"/><path d="M9 19l-2 7 7-3 7 3-2-7" stroke="#fff" stroke-width="2" fill="none"/></svg></div>
<div class="step-icon" style="left:568px;top:2832px"><svg width="28" height="28"><path d="M4 24V12l10-7 10 7v12z" fill="none" stroke="#fff" stroke-width="2"/><rect x="11" y="15" width="6" height="9" fill="none" stroke="#fff" stroke-width="2"/></svg></div>

<div class="step left" style="left:115px;top:2552px"><h4>CONSULTATION</h4>Lorem ipsum dolor sit amet, consectetur adipiscing elit, sed do eiusmod tempor et dolore magna aliqua.</div>
<div class="step left" style="left:115px;top:2734px"><h4>CUSTOMIZED PLAN GENERATION</h4>Lorem ipsum dolor sit amet, consectetur adipiscing elit, sed do eiusmod tempor et dolore magna aliqua.</div>
<div class="step" style="left:815px;top:2552px"><h4>OPERATIONS TRAINING</h4>Lorem ipsum dolor sit amet, consectetur adipiscing elit, sed do eiusmod tempor et dolore magna aliqua.</div>
<div class="step" style="left:815px;top:2734px"><h4>INSTALLATION</h4>Lorem ipsum dolor sit amet, consectetur adipiscing elit, sed do eiusmod tempor et dolore magna aliqua.</div>
<div class="step" style="left:370px;top:2907px;width:460px;text-align:center"><h4>EVACUATION &amp; PROCUREMENT</h4>Lorem ipsum dolor sit amet, consectetur adipiscing elit, sed do eiusmod<br>tempor et dolore magna aliqua.</div>

<!-- case study -->
<h2 class="section-title" style="top:3073px">CASE <span class="accent">STUDY</span></h2>

<article class="case" style="left:111px">
  <div class="photo" role="img" aria-label="Aerial photo of a housing development under construction" style="background:linear-gradient(180deg,#6a5a3a,#a37a47 45%,#8b6a40 70%,#5a4a30)"></div>
  <span class="date">AUG 15, 2020</span>
  <h3>Lorem ipsum dolor consectetur &nbsp;elit,</h3>
  <p>Sed ut perspiciatis unde omnis iste natus sit voluptatem accusantium</p>
  <span class="link">READ MORE <svg width="13" height="13"><circle cx="6.5" cy="6.5" r="5.5" fill="none" stroke="#1a9e9b" stroke-width="1.6"/><path d="M5.5 4L8 6.5 5.5 9" stroke="#1a9e9b" stroke-width="1.6" fill="none"/></svg></span>
</article>
<article class="case" style="left:445px">
  <div class="photo" role="img" aria-label="Photo of a modern senior living building under a cloudy sky" style="background:linear-gradient(180deg,#2f5f96,#9bb3cc 40%,#5b6066 65%,#4f7a3a)"></div>
  <span class="date">AUG 15, 2020</span>
  <h3>Lorem ipsum dolor consectetur &nbsp;elit,</h3>
  <p>Sed ut perspiciatis unde omnis iste natus sit voluptatem accusantium</p>
  <span class="link">READ MORE <svg width="13" height="13"><circle cx="6.5" cy="6.5" r="5.5" fill="none" stroke="#1a9e9b" stroke-width="1.6"/><path d="M5.5 4L8 6.5 5.5 9" stroke="#1a9e9b" stroke-width="1.6" fill="none"/></svg></span>
</article>
<article class="case" style="left:779px">
  <div class="photo" role="img" aria-label="Photo of hands washing under a touchless kitchen faucet" style="background:linear-gradient(135deg,#3a3a3a,#8a8a8a 45%,#c9b8b0 70%,#6a6a6a)"></div>
  <span class="date">AUG 15, 2020</span>
  <h3>Lorem ipsum dolor consectetur &nbsp;elit,</h3>
  <p>Sed ut perspiciatis unde omnis iste natus sit voluptatem accusantium</p>
  <span class="link">READ MORE <svg width="13" height="13"><circle cx="6.5" cy="6.5" r="5.5" fill="none" stroke="#1a9e9b" stroke-width="1.6"/><path d="M5.5 4L8 6.5 5.5 9" stroke="#1a9e9b" stroke-width="1.6" fill="none"/></svg></span>
</article>

<!-- footer -->
<footer class="abs site-footer">
  <div class="abs foot-brand">SAGECARE</div>
  <p class="abs foot-about">Lorem ipsum dolor sit amet, consectetur adipiscing elit, sed do eiusmod tempor incididunt ut labore et dolore magna aliqua.</p>
  <div class="abs social">
    <svg width="12" height="14"><circle cx="6" cy="7" r="5" fill="#fff"/></svg>
    <svg width="14" height="14"><circle cx="7" cy="7" r="5" fill="#fff"/></svg>
    <svg width="14" height="14"><circle cx="7" cy="7" r="5" fill="#fff"/></svg>
    <svg width="14" height="14"><circle cx="7" cy="7" r="5" fill="#fff"/></svg>
  </div>

  <div class="abs" style="left:377px;top:68px;width:230px">
    <h4>Our Office Address</h4>
    <div style="margin-top:22px">
      <div class="contact-item"><svg width="12" height="12" viewBox="0 0 24 24"><path fill="#5cc3bf" d="M6.6 10.8a15 15 0 006.6 6.6l2.2-2.2c.3-.3.7-.4 1-.2 1.1.4 2.3.6 3.6.6.6 0 1 .4 1 1V20c0 .6-.4 1-1 1A17 17 0 013 4c0-.6.4-1 1-1h3.5c.6 0 1 .4 1 1 0 1.3.2 2.5.6 3.6.1.3 0 .7-.2 1z"/></svg><div><b>Phone</b><br>888 888 8888</div></div>
      <div class="contact-item"><svg width="12" height="12" viewBox="0 0 12 12"><rect x="0.5" y="2" width="11" height="8" fill="#5cc3bf"/><path d="M1 2.5l5 4 5-4" stroke="#15196b" fill="none"/></svg><div><b>Email</b><br>info@sagecare.example</div></div>
      <div class="contact-item"><svg width="12" height="14" viewBox="0 0 12 14"><path d="M6 0a5 5 0 00-5 5c0 4 5 9 5 9s5-5 5-9a5 5 0 00-5-5z" fill="#5cc3bf"/><circle cx="6" cy="5" r="2" fill="#15196b"/></svg><div><b>Location</b><br>939 Lorem ipsum dolor sit amet,<br>consectetur elit,</div></div>
    </div>
  </div>

  <div class="abs" style="left:680px;top:68px">
    <h4>Company</h4>
    <div class="foot-links">Products<br>Technology<br>Benefits<br>Marketing<br>Process<br>Case study</div>
  </div>

  <div class="abs" style="left:862px;top:68px;width:230px">
    <h4>Stil have questios?</h4>
    <p style="font-size:12px;line-height:19px;margin-top:22px">Contact us using this form. A representative will aswer your questions as soon as possible.</p>
    <div class="btn-touch">GET IN TOUCH</div>
  </div>

  <div class="abs go-up"><svg width="9" height="9"><path d="M4.5 1v8M1 4.5L4.5 1 8 4.5" stroke="#15196b" stroke-width="1.8" fill="none"/></svg>Go Up</div>

  <div class="abs legal">
    <span>© 2020 Sagecare | All Rights Reserved</span>
    <span>Privacy Policy &nbsp;| &nbsp;Cookie Policy &nbsp;| &nbsp;Terms Of Services</span>
  </div>
</footer>

</body>
</html>
```